Successful Health Company Needs a Face Lift

We need a beautiful new design for our existing, online health supplements business.

Most of the elements are already there, but we need your sophistication and style.

The 3 pages that need your magic touch are:
Home page:
http://www.vitabrook.co.uk

Multiple Product pages. e.g:
http://www.vitabrook.co.uk/health-issues/major-organs/skin-hair-nails.html

Single Product pages. e.g:
http://www.vitabrook.co.uk/l-arginine-500-mg.html

Please have a look around.

This is a bilingual site, so all text (except logo) needs to be easily changed/translated. If photoshop files can be provided where we can simply translate the text layer of a graphic, that is acceptable. Please note that Greman words are generally longer than English.

Appearance:
The over all look should be open, light, uplifting and sophisticated.

The Home Page in detail:
We are largely happy with the category boxes in the centre column although you may restyle these if you wish.
The header, left menu and right column don't hang together and need your skills.

Logo:
We would like you to enhance our logo, but please note the 'S' and circle are used on many product labels, so we can't go too far from this just now.
(Product label example: http://www.vitabrook.co.uk/black-walnut-tincture-from-green-hull.html)

Header:
This needs to imply health and be light and stylish without it taking up valuable room.

Left Menu:
This is a multi-layer concertina menu. It is hard to see where your are within it. It needs to be made more clear and easy to navigate, maybe by using indentation and or better colour choices.
Please show it expanded and condensed in your design proposals.
(Extended menu example: http://www.vitabrook.co.uk/health-issues/female-health/thrush.html)

Multiple Product pages in detail
Please style the the brief descriptions, which must contain bullet points, price, add to basket and learn more.

Single Product pages in detail
The design and layout of this page needs to include all the elements currently there, including price, Qty, Add to Basket button, size and article number.

The static blocks on the right column will appear on these single product pages and need to suit the design well. They should not over-power the central content of the page.
Updates

Thank you all for participating.

Please note that what we are looking for is a more stylish and attractive version of what we already have.  The elements are all there.  We are not looking for a new concept.

We are happy for designers to switch images for better ones, work with colour ways, alter proportions and insert the elements in our brief.

We do not want to add banners, large images etc.  We want our customers to be familiar with what they see, and to be impressed with how much better the pages hang together.  They should not think they've landed at a new company.

We do want to see how the left menu looks when extended to show 2nd and 3rd tier menu titles.
We will also want to see how the design works for a multiple product page like this: http://www.vitabrook.co.uk/supplement-type/anti-microbials.html
as well as a single product page like this:  http://www.vitabrook.co.uk/black-walnut-extract.html

Some adjustment to the 'VitaBrook' logo is also an option and the graphic has been attached. 

Thank you for your careful attention to our brief.

Marcus.
pp Leopold

Project Deadline Extended
Reason: Due to unanticipated travel arrangements, the company director will only be available to make final decisions on Monday the 19th of March. Please continue updating submissions as we are in touch. Thank you for your understanding.

Target Market(s)

Health conscious women 70% men 30% aged 40 to 65 and health practitioners.

Industry/Entity Type

Health

Requirements
Must have
• Please include in the Header:
UK and German flags
Facebook, dig, +1, twitter, linked in, stumble upon
Padlock/SSL security/secure transaction
Practitioner helpline/ orders phone number
Paypal/Credit card logo

Please include in right column:
Clinician Corner
Mercury Free Dentistry
Shopping Basket
Storefronts for Therapists

Please include in either Header or Right Column
Same day dispatch
Money back warranty

```html
<!DOCTYPE html>
<html lang="en">
<head>
<meta charset="utf-8">
<title>VitaBrook – Home</title>
<link href="https://fonts.googleapis.com/css2?family=Arimo:wght@400;700&family=Cousine:wght@400;700&display=swap" rel="stylesheet">
<style>
:root{
  --page-bg:#f2f2f2;
  --frame:#c4c4c4;
  --pink:#cc3d84;
  --pink-soft:#e05a9a;
  --red:#e8141e;
  --cyan:#b4ecf3;
  --cyan-soft:#ddf3f7;
  --teal:#2b8aa6;
  --teal-dark:#236e80;
  --link-blue:#1a3fd6;
  --footer-link:#4db6cc;
  --text:#333;
  --line:#dcdcdc;
}
*{box-sizing:border-box;margin:0;padding:0}
html,body{width:1180px;height:1200px;overflow:hidden}
body{background:var(--page-bg);font-family:"Arimo",Arial,sans-serif;color:var(--text);position:relative}
ul{list-style:none}
a{color:inherit;text-decoration:none}
h2,h3{font-weight:400}
.abs{position:absolute}

.page{position:absolute;left:70px;top:15px;width:1015px;height:1150px;background:#fff;border:1px solid var(--frame);border-radius:10px}

/* header */
.brand{position:absolute;left:97px;top:52px;font-size:32px;color:var(--pink-soft);letter-spacing:1px;font-weight:400}
.account{position:absolute;top:33px;display:flex;gap:15px;left:842px}
.account a{display:block;height:28px;line-height:28px;background:#eee;border-radius:5px;font-size:13px;text-align:center;color:#222}
.account a.basket{width:96px}.account a.login{width:100px}
.main-nav a{position:absolute;top:143px;font-size:13px;color:#333}
.search{position:absolute;left:597px;top:129px;width:230px;height:29px;background:#f0f0f0;border-radius:2px;font-size:13px;color:#aaa;padding:8px 11px}
.search svg{position:absolute;right:2px;top:2px}
.secure{position:absolute;left:856px;top:110px}
.phone{position:absolute;left:891px;top:108px;font-size:26px;color:var(--pink);letter-spacing:.3px}
.cards{position:absolute;left:892px;top:137px;display:flex;gap:3px}
.cards span{width:30px;height:16px;border-radius:3px}
.header-fade{position:absolute;left:71px;top:163px;width:1013px;height:18px;background:linear-gradient(#f6f6f6,#fff)}

/* category boxes */
.cat{position:absolute;border:1px solid var(--line);border-radius:6px;background:#fff}
.cat-tab{position:absolute;height:26px;padding:0 18px;line-height:26px;background:var(--cyan-soft);border-radius:13px;font-family:"Cousine",monospace;font-size:14px;font-weight:400;color:var(--pink);letter-spacing:.3px;white-space:nowrap}
.cat-photo{position:absolute;left:0;top:0;bottom:0;border-radius:6px 0 0 6px}
.cat-links{position:absolute;font-family:"Cousine",monospace;font-size:11.5px;color:var(--pink);line-height:23px}
.cat-links li{padding-left:17px;position:relative;white-space:nowrap}
.cat-links li::before{content:"›";position:absolute;left:0;top:6px;width:11px;height:11px;border:1px solid #ececec;border-radius:50%;font-size:11px;line-height:9px;text-align:center;color:var(--red)}
.cat-links .group{font-size:14px;font-weight:700;color:var(--teal-dark);padding-left:14px}
.cat-links .group::before{display:none}
.cat-links.compact{font-size:11px}

/* categories panel */
.categories{position:absolute;left:627px;top:196px;width:220px;height:561px;background:var(--cyan-soft);border-radius:8px}
.categories h2{position:absolute;left:18px;top:14px;font-size:18px;color:var(--teal)}
.cat-menu{position:absolute;left:11px;top:42px;width:198px;height:507px;background:#fff;border:1px solid #cfe6ec;border-radius:6px}
.cat-menu li{position:absolute;left:0;right:0;font-size:13px;color:var(--pink);padding-left:27px}
.cat-menu li::before{content:"›";position:absolute;left:9px;top:1px;width:11px;height:11px;border:1px solid #ececec;border-radius:50%;font-size:10px;line-height:9px;text-align:center;color:#999}
.cat-menu .has-sub::after{content:"+";position:absolute;right:12px;top:-1px;width:15px;height:15px;border:1px solid #aaa;border-radius:50%;font-size:14px;line-height:13px;text-align:center;color:#888}
.cat-menu .offers{color:var(--red)}
.cat-menu .offers::before{display:none}

/* right column */
.side-box{position:absolute;border:1px solid #dcdcdc;background:#fff}
.side-head{background:var(--cyan);color:var(--pink-soft);font-size:15px;padding:3px 8px;line-height:18px}
.cart{position:absolute;left:857px;top:197px;width:206px;height:71px;background:#ececec}
.cart h3{font-size:12px;color:#777;font-weight:700;position:absolute;left:32px;top:6px}
.cart svg{position:absolute;left:8px;top:5px}
.cart p{position:absolute;left:7px;top:25px;width:193px;height:38px;background:#fff;border-radius:3px;font-size:12px;color:#888;padding:12px 14px}
.help p{font-size:14px;color:var(--pink-soft);line-height:17px}
.find-link{display:inline-block;border:1px solid #999;padding:0 2px;color:var(--link-blue);text-decoration:underline;font-size:14px;letter-spacing:-.5px}
.photo-slot{position:absolute}
.partner{position:absolute;left:862px;top:410px;width:205px;height:76px;background:linear-gradient(90deg,#7cc6ec,#e8f5fc 60%,#fff);border-bottom:6px solid #e03b2a}
.webshop{position:absolute;left:857px;top:515px;width:205px;height:77px}
.webshop .t1{position:absolute;left:52px;top:0;font-size:22px;color:var(--red)}
.webshop .t2{position:absolute;left:95px;top:26px;font-size:16px;color:var(--red)}
.webshop .t3{position:absolute;left:65px;top:44px;font-size:21px;color:var(--red)}
.side-link{color:var(--link-blue);text-decoration:underline;font-size:14px;line-height:18px}
.newsletter label{display:block;font-weight:700;font-size:14px;color:#555;line-height:18px}
.newsletter .field{width:173px;height:27px;border:1px solid #bbb;margin-top:4px}
.subscribe{margin-top:3px;width:96px;height:30px;border:1px solid #9dc8e6;border-radius:3px;background:linear-gradient(#e6f3fc,#c9e3f6);color:#1646a8;font-weight:700;font-size:15px;text-align:center;line-height:28px}

/* social strip */
.social{position:absolute;left:1086px;top:275px;width:40px;height:225px;background:#fff;box-shadow:0 0 3px rgba(0,0,0,.25)}
.social span{position:absolute;left:6px;width:32px;height:32px;border-radius:3px}

/* footer */
.footer-tags{position:absolute;left:85px;width:985px;text-align:center;font-size:13px;color:var(--footer-link)}
.footer-tags a{margin:0 10px}
.footer-nav{position:absolute;left:85px;top:1061px;width:985px;text-align:center;font-size:14px;color:var(--link-blue)}
.footer-nav a{margin:0 8px}
.legal{position:absolute;left:85px;width:985px;text-align:center;font-size:14px;color:#888}
.legal.bold{font-weight:700}
</style>
</head>
<body>
<div class="page"></div>

<header>
  <a class="brand" href="#">VITABROOK</a>
  <nav class="account"><a class="basket" href="#">My Basket</a><a class="login" href="#">Login</a></nav>
  <nav class="main-nav"><a href="#" style="left:97px">Home</a><a href="#" style="left:173px">Detox</a><a href="#" style="left:247px">Hydration</a><a href="#" style="left:341px">Supplements</a><a href="#" style="left:455px">Your Health Issues</a></nav>
  <div class="search">Search
    <svg width="34" height="26" viewBox="0 0 34 26"><circle cx="13" cy="11" r="8" fill="none" stroke="#bbb" stroke-width="3"/><line x1="19" y1="17" x2="29" y2="24" stroke="#bbb" stroke-width="4" stroke-linecap="round"/></svg>
  </div>
  <svg class="secure" width="32" height="48" viewBox="0 0 32 48" aria-label="Secure checkout padlock"><path d="M7 22V13a9 9 0 0 1 18 0v9" fill="none" stroke="#999" stroke-width="4"/><rect x="2" y="21" width="28" height="25" rx="3" fill="#d4a52a"/></svg>
  <div class="phone">01632 960 418</div>
  <div class="cards" aria-label="Accepted payment methods">
    <span style="background:#e8a020"></span><span style="background:#1a3f9a"></span><span style="background:#5a8fcf"></span><span style="background:#2f6fc9"></span><span style="background:#dfe7f5"></span>
  </div>
</header>
<div class="header-fade"></div>

<main>
  <section class="cat" style="left:85px;top:200px;width:260px;height:127px">
    <div class="cat-photo" role="img" aria-label="Woman holding her waist, green towel" style="width:120px;background:linear-gradient(160deg,#eed8c8,#d8b59c 55%,#8cc860)"></div>
    <ul class="cat-links" style="left:133px;top:12px"><li>Colon Cleanse</li><li>Constipation</li><li>Candida</li><li>Irritable Bowel</li><li>Bloating &amp; Wind</li></ul>
  </section>
  <h2 class="cat-tab" style="left:90px;top:183px">DIGESTION</h2>

  <section class="cat" style="left:355px;top:200px;width:260px;height:127px">
    <div class="cat-photo" role="img" aria-label="Man holding his lower back" style="width:128px;background:linear-gradient(160deg,#9a9a9a,#d8d0cc 55%,#c9b2a8)"></div>
    <ul class="cat-links" style="left:141px;top:14px;line-height:24px"><li>Back Pain</li><li>Joint and Bone</li><li>Headaches</li><li>Period Pain</li></ul>
  </section>
  <h2 class="cat-tab" style="left:360px;top:188px">PAIN</h2>

  <section class="cat" style="left:85px;top:350px;width:260px;height:127px">
    <div class="cat-photo" role="img" aria-label="Waist with tape measure" style="width:118px;background:linear-gradient(160deg,#f3ded0,#e7c4ae 60%,#cfe4f0)"></div>
    <ul class="cat-links" style="left:126px;top:26px;line-height:24px"><li>Without Dieting</li><li>Supplements</li><li>Sugar Metabolism</li></ul>
  </section>
  <h2 class="cat-tab" style="left:90px;top:336px">WEIGHT LOSS</h2>

  <section class="cat" style="left:355px;top:350px;width:260px;height:127px">
    <div class="cat-photo" role="img" aria-label="Pink lily on white towels" style="width:112px;background:linear-gradient(150deg,#f3e4ec,#e07aa8 45%,#eceae8)"></div>
    <ul class="cat-links" style="left:115px;top:14px;line-height:22px"><li>Heavy Metal Detox</li><li>Parasite Cleanse</li><li>Kidney Cleanse</li><li>Liver Cleanse</li><li>Colon Cleanse</li></ul>
  </section>
  <h2 class="cat-tab" style="left:358px;top:337px">DETOX &amp; CLEANING</h2>

  <section class="cat" style="left:85px;top:500px;width:260px;height:128px">
    <div class="cat-photo" role="img" aria-label="Woman with flowers in her hair" style="width:128px;background:linear-gradient(160deg,#fff,#d9b49c 45%,#6d4a3a)"></div>
    <ul class="cat-links" style="left:141px;top:8px"><li>Anti Aging</li><li>Cosmetics</li><li>Skin Range</li><li>Face &amp; Mouth</li><li>Hair Care</li></ul>
  </section>
  <h2 class="cat-tab" style="left:90px;top:484px">BODY CARE</h2>

  <section class="cat" style="left:357px;top:500px;width:258px;height:128px">
    <div class="cat-photo" role="img" aria-label="Model of a human brain" style="width:110px;background:radial-gradient(circle at 50% 55%,#d8d8d8,#f4f4f4 70%,#fff)"></div>
    <ul class="cat-links" style="left:111px;top:22px"><li>Memory</li><li>Headaches</li><li>Cognitive Function</li><li>Mood &amp; Sleep</li></ul>
  </section>
  <h2 class="cat-tab" style="left:360px;top:484px">BRAIN HEALTH</h2>

  <section class="cat" style="left:85px;top:648px;width:260px;height:127px">
    <div class="cat-photo" role="img" aria-label="Woman drinking from a water bottle" style="width:115px;background:linear-gradient(100deg,#e6b49c,#f0d6c8 45%,#e8eef4 75%,#fff)"></div>
    <ul class="cat-links" style="left:118px;top:33px"><li>Water Filtration</li><li>Electrolytes</li><li>Super-Hydration</li></ul>
  </section>
  <h2 class="cat-tab" style="left:90px;top:634px">WATER &amp; HYDRATION</h2>

  <section class="cat" style="left:357px;top:648px;width:258px;height:127px">
    <div class="cat-photo" role="img" aria-label="Stethoscope with a medical shield" style="width:120px;background:radial-gradient(circle at 55% 45%,#7fb6e8,#d4e6f6 55%,#fff)"></div>
    <ul class="cat-links" style="left:135px;top:22px"><li>Zapping</li><li>Cardiovascular</li><li>Ozone</li><li>Allergy Test</li></ul>
  </section>
  <h2 class="cat-tab" style="left:365px;top:637px">HEALTH DEVICES</h2>

  <section class="cat" style="left:85px;top:800px;width:258px;height:175px">
    <div class="cat-photo" role="img" aria-label="Male and female symbols" style="width:95px;background:linear-gradient(160deg,#f4f4f4,#cfe6ea 55%,#f4f4f4)"></div>
    <ul class="cat-links compact" style="left:101px;top:12px;line-height:20px">
      <li class="group">Female Health</li><li>Breast Health</li><li>Menopause</li><li>Menstruation &amp; PMS</li>
      <li class="group">Male Health</li><li>Erectile Dysfunction</li><li>Hair Loss.</li><li>Prostate Health</li>
    </ul>
  </section>
  <h2 class="cat-tab" style="left:88px;top:788px">HEALTH</h2>

  <section class="cat" style="left:359px;top:800px;width:258px;height:175px">
    <div class="cat-photo" role="img" aria-label="Anatomical heart" style="width:115px;background:radial-gradient(circle at 45% 45%,#c8572f,#e8a07c 45%,#fff 75%)"></div>
    <ul class="cat-links" style="left:122px;top:69px"><li>Blood Pressure</li><li>Cholesterol</li><li>Heart &amp; Arteries</li></ul>
  </section>
  <h2 class="cat-tab" style="left:370px;top:789px">CARDIOVASCULAR</h2>

  <nav class="categories">
    <h2>Categories</h2>
    <ul class="cat-menu">
      <li class="has-sub" style="top:14px">Supplement Type</li>
      <li class="has-sub" style="top:44px">Your Health Issue</li>
      <li class="has-sub" style="top:74px">Expert Product Lines</li>
      <li class="has-sub" style="top:134px">Detox &amp; Cleansing</li>
      <li class="has-sub" style="top:164px">Water &amp; Hydration</li>
      <li class="has-sub" style="top:194px">Natural Body Care</li>
      <li style="top:254px">Sport &amp; Fitness</li>
      <li style="top:284px">Health Technology</li>
      <li style="top:314px">Household Products</li>
      <li style="top:374px">Laboratory Tests</li>
      <li style="top:404px">Books &amp; Education</li>
      <li class="offers" style="top:451px">New &amp; Special Offers</li>
    </ul>
  </nav>
</main>

<aside>
  <div class="cart">
    <svg width="18" height="16" viewBox="0 0 18 16"><path d="M1 2h3l2 8h9l2-6H5" fill="none" stroke="#888" stroke-width="1.5"/><circle cx="7" cy="13" r="1.5" fill="#888"/><circle cx="14" cy="13" r="1.5" fill="#888"/></svg>
    <h3>SHOPPING CART</h3>
    <p>Your cart is empty.</p>
  </div>

  <section class="side-box help" style="left:861px;top:282px;width:202px;height:111px">
    <div class="side-head">PRACTITIONER HELP ?</div>
    <div style="padding:10px 20px">
      <p>PLEASE CALL:</p>
      <p>01632 - 960 418</p>
      <p style="font-size:10px;color:#999;line-height:10px;margin-left:-6px">or</p>
      <a class="find-link" href="#">Find a Practitioner</a>
    </div>
    <div class="photo-slot" role="img" aria-label="Doctor with stethoscope" style="left:135px;top:25px;width:64px;height:82px;background:linear-gradient(#e6eef4,#c8d4de)"></div>
  </section>

  <div class="partner" role="img" aria-label="Partner supplier banner"></div>

  <div class="webshop">
    <div class="photo-slot" role="img" aria-label="Hand pointing right" style="left:0;top:5px;width:60px;height:68px;background:linear-gradient(90deg,#e8b89a,#f4dccc)"></div>
    <span class="t1">Free Webshop</span><span class="t2">for our</span><span class="t3">practitioners</span>
  </div>

  <section class="side-box" style="left:859px;top:603px;width:199px;height:115px">
    <div class="side-head">CLINICIAN CORNER</div>
    <p style="padding:26px 12px"><a class="side-link" href="#">Contact a Natural<br>Health Practitioner</a></p>
    <div class="photo-slot" role="img" aria-label="Smiling woman portrait" style="left:130px;top:28px;width:57px;height:75px;background:linear-gradient(#e0c4b0,#b0846c)"></div>
  </section>

  <section class="side-box" style="left:859px;top:729px;width:199px;height:98px">
    <div class="side-head">MERCURY FREE<br>DENTIST UK &amp; IRELAND</div>
    <p style="padding:9px 12px;font-size:14px;line-height:18px">A comprehensive<br>list <a class="side-link" href="#">available here.</a></p>
    <div class="photo-slot" role="img" aria-label="Smile with white teeth" style="left:138px;top:46px;width:49px;height:38px;background:linear-gradient(#f0d8d8,#fff)"></div>
  </section>

  <section class="side-box newsletter" style="left:859px;top:839px;width:199px;height:133px">
    <div class="side-head">NEWSLETTER</div>
    <div style="padding:4px 10px">
      <label>Sign up for our<br>newsletter:</label>
      <div class="field"></div>
      <div class="subscribe">Subscribe</div>
    </div>
  </section>
</aside>

<div class="social" aria-label="Share links">
  <span style="top:6px;height:22px;background:#e6e6e6"></span>
  <span style="top:36px;background:#3b5998"></span>
  <span style="top:73px;background:#5cb6e0"></span>
  <span style="top:110px;background:#0e76a8"></span>
  <span style="top:147px;background:#9aa4ae"></span>
  <span style="top:184px;background:#3c8a3f"></span>
</div>

<footer>
  <div class="footer-tags" style="top:986px"><a>Kidney Pain</a><a>Kidney Stones</a><a>Kidney Disease Symptoms</a><a>Colon Cleanse</a><a>Digestive Enzymes</a><a>Digestive Enzymes Supplement</a><a>Healing Principles</a></div>
  <div class="footer-tags" style="top:1007px"><a>Herbal Remedies</a><a>Herbal Remedies for Anxiety</a><a>Herbal Remedies for Constipation</a><a>Herbal Remedies for Depression</a><a>Herbal Remedies for Menopause</a></div>
  <div class="footer-tags" style="top:1029px"><a>Bloated Stomach</a><a>Health Shops</a><a>Digenta</a><a>What is Mercury Free Dentistry?</a></div>
  <nav class="footer-nav"><a>About Us</a><a>Search Terms</a><a>Advanced Search</a><a>Terms &amp; Conditions</a><a>Privacy Policy</a><a>Contact Us</a></nav>
  <p class="legal bold" style="top:1092px">© 2010 VitaBrook. All Rights Reserved.</p>
  <p class="legal" style="top:1114px">Please note: This information is provided for educational purposes only. Medical advice is neither implied nor intended.</p>
  <p class="legal" style="top:1136px">Please consult a health professional for medical advice.</p>
</footer>
</body>
</html>
```